Banner Ad Design Project

We would like to create a banner for Venkro to attract designers to use our platform.
Guidelines:
Animated Banner (GIF)
50k max file size
Animation loops and stops after 30 secs
Design Instructions:
Design should be clean and based on the color schemes of the site: http://www.venkro-example.com/designer to get a sense of the site, fill the form.
Copy:
Are you a Designer?
Join venkro and earn money
Call to action:
Sign up NOW!
Banner size is 300*250

```html
<!DOCTYPE html>
<html lang="en">
<head>
<meta charset="utf-8">
<title>Venkro – Designer Banner Set</title>
<link rel="stylesheet" href="https://fonts.googleapis.com/css2?family=Oswald:wght@500&family=Source+Sans+3:wght@700&display=swap">
<style>
  :root {
    --stage: #6e4b30;
    --blue: #3c9be0;
    --crimson: #c71850;
    --green: #8bb83f;
    --footer: #2c2c2c;
    --white: #ffffff;
    --figure-dark: #262b31;
    --figure-light: #56606b;
  }
  * { margin: 0; padding: 0; box-sizing: border-box; }
  html, body {
    width: 1200px; height: 838px; overflow: hidden;
    background: var(--stage);
  }
  .stage { position: relative; width: 1200px; height: 838px; }

  .banner {
    position: absolute; top: 255px;
    width: 367px; height: 305px;
    box-shadow: 0 6px 14px rgba(0,0,0,.45);
    overflow: hidden;
    font-family: "Source Sans 3", "Source Sans Pro", sans-serif;
    color: var(--white);
  }
  .banner--designer { left: 29px; --accent: var(--blue); }
  .banner--join { left: 413px; --accent: var(--crimson); }
  .banner--earn { left: 794px; --accent: var(--green); }

  .banner__panel {
    position: absolute; left: 0; top: 0;
    width: 100%; height: 245px;
    background: var(--accent);
  }

  .banner__footer {
    position: absolute; left: 0; bottom: 0;
    width: 100%; height: 60px;
    background: var(--footer);
  }
  .brand-name {
    position: absolute; left: 37px; top: 12px;
    font-size: 32px; font-weight: 700; letter-spacing: -0.5px;
    line-height: 1; color: var(--white);
  }
  .cta {
    position: absolute; left: 166px; top: 20px;
    font-size: 18px; font-weight: 700; line-height: 1;
    letter-spacing: 0.1px; white-space: nowrap;
  }
  .cta__chevron { color: var(--accent); font-size: 21px; margin: 0 6px; }
  .cta__chevron:first-child { margin-left: 0; }

  .headline--question {
    position: absolute; left: 20px; top: 10px; z-index: 2;
    font-family: "Oswald", "Arial Narrow", sans-serif;
    font-weight: 500; font-size: 31px; line-height: 38px;
    text-transform: uppercase; letter-spacing: 0.2px;
    white-space: nowrap;
  }
  .figure-area {
    position: absolute; right: 0; top: 0;
    width: 170px; height: 245px;
    background: linear-gradient(160deg, var(--figure-light), var(--figure-dark));
  }

  .headline--statement {
    position: absolute;
    text-align: center;
    font-size: 31px; font-weight: 700; line-height: 38px;
    text-transform: uppercase; letter-spacing: 0.5px;
    white-space: nowrap;
  }
  .banner--join .headline--statement { top: 115px; left: 29px; width: 232px; }
  .banner--earn .headline--statement { top: 82px; left: 28px; width: 300px; }

  .exclaim {
    position: absolute; top: 16px; left: 300px;
    width: 43px; height: 213px;
    filter: drop-shadow(-3px 3px 3px rgba(0,0,0,.35));
  }
  .banner--earn .exclaim { left: 301px; width: 40px; }
</style>
</head>
<body>
<main class="stage">

  <section class="banner banner--designer">
    <div class="banner__panel">
      <div class="figure-area" role="img" aria-label="Illustration of a man in a suit pointing at the viewer"></div>
      <h2 class="headline--question">Are you<br>a designer?</h2>
    </div>
    <footer class="banner__footer">
      <span class="brand-name">venkro</span>
      <span class="cta"><span class="cta__chevron">»</span>SIGN UP NOW<span class="cta__chevron">«</span></span>
    </footer>
  </section>

  <section class="banner banner--join">
    <div class="banner__panel">
      <h2 class="headline--statement">Join us</h2>
      <svg class="exclaim" viewBox="0 0 43 213" aria-hidden="true">
        <polygon points="0,0 43,0 35,148 8,148" fill="#fff"/>
        <rect x="5" y="172" width="33" height="41" fill="#fff"/>
      </svg>
    </div>
    <footer class="banner__footer">
      <span class="brand-name">venkro</span>
      <span class="cta"><span class="cta__chevron">»</span>SIGN UP NOW<span class="cta__chevron">«</span></span>
    </footer>
  </section>

  <section class="banner banner--earn">
    <div class="banner__panel">
      <h2 class="headline--statement">And<br>earn money</h2>
      <svg class="exclaim" viewBox="0 0 43 213" preserveAspectRatio="none" aria-hidden="true">
        <polygon points="0,0 43,0 35,148 8,148" fill="#fff"/>
        <rect x="5" y="172" width="33" height="41" fill="#fff"/>
      </svg>
    </div>
    <footer class="banner__footer">
      <span class="brand-name">venkro</span>
      <span class="cta"><span class="cta__chevron">»</span>SIGN UP NOW<span class="cta__chevron">«</span></span>
    </footer>
  </section>

</main>
</body>
</html>
```